Shipping Container Sales & Leasing Flyer

We need a flyer that is going to be presented and left behind while prospecting potential customers. The service we are selling is the sale, rental and customization of 20' and 40' shipping containers.

We provide new and used containers to customers for various reasons, mainly storage. We also custom modify containers into storage units, mobile offices, mobile job site storage, command centers, pump houses, garages, living space, the only limit is the customers imagination.

I would like our company logo and phone / email at the bottom but the design should showcase some of the attached images ive provided as examples and have spots where we can list the types of equipment we have for sale and the various types of conversions we can offer.

Please also tie in to the colour scheme of our logo.

Target Market(s)

Moving & Storage, Construction, Contractors, Business to Business, Any business that needs portable storage, Landscapers, Property Maintenance companies.

Industry/Entity Type

Shipping

Font styles to use
Serif
Sans Serif

Requirements
Must have
• Professional feel, clean original design.
Nice to have
• Tie in to our logo colour scheme.
Should not have
• Bulky or crowded look

```html
<!DOCTYPE html>
<html lang="en">
<head>
<meta charset="utf-8">
<title>Corran Management – Container Flyer</title>
<link rel="stylesheet" href="https://fonts.googleapis.com/css2?family=Oswald:wght@400;500;600&family=Open+Sans:wght@400;600&display=swap">
<style>
  :root{
    --charcoal:#34383b;
    --charcoal-deep:#25282a;
    --slate:#50565a;
    --green:#7cc242;
    --green-dark:#4f9a2c;
    --lime:#b5d98a;
    --navy:#2f3f73;
    --white:#ffffff;
    --ink:#2b2e31;
  }
  *{margin:0;padding:0;box-sizing:border-box}
  html,body{width:900px;height:1200px;overflow:hidden;background:var(--charcoal-deep)}
  .flyer{position:relative;width:900px;height:1200px;overflow:hidden;background:var(--charcoal)}
  .flyer-shapes{position:absolute;inset:0}
  .brand{
    position:absolute;left:300px;top:520px;width:200px;text-align:center;
    font-family:"Oswald",sans-serif;font-weight:500;color:var(--green-dark);
    letter-spacing:2px;line-height:1.1;font-size:24px;text-transform:uppercase;
  }
  .brand-mark{display:block;width:34px;height:34px;border-radius:50%;background:var(--green);margin:0 auto 10px}
  .headline{
    position:absolute;left:470px;top:598px;width:400px;text-align:right;
    font-family:"Oswald",sans-serif;font-weight:500;text-transform:uppercase;line-height:1.02;
  }
  .headline .accent{display:block;color:var(--green);font-size:40px}
  .headline .dark{display:block;color:var(--ink);font-size:40px;font-weight:400}
  .uses{
    position:absolute;top:762px;list-style:none;
    font-family:"Open Sans",sans-serif;font-size:13.5px;color:var(--ink);line-height:1.45;
  }
  .uses li{position:relative;padding-left:16px;margin-bottom:2px}
  .uses li::before{content:"";position:absolute;left:0;top:7px;width:7px;height:7px;border-radius:50%;background:var(--green)}
  .uses-main{left:440px;width:210px}
  .uses-more{left:680px;width:190px}
  .call{
    position:absolute;left:430px;top:1118px;width:440px;text-align:right;
    font-family:"Oswald",sans-serif;font-weight:500;font-size:36px;color:var(--green);
    letter-spacing:1px;text-transform:uppercase;
  }
  .call .number{color:var(--white);margin-left:12px}
</style>
</head>
<body>
<main class="flyer">
  <svg class="flyer-shapes" width="900" height="1200" viewBox="0 0 900 1200" xmlns="http://www.w3.org/2000/svg">
    <defs>
      <linearGradient id="skyPhoto" x1="0" y1="0" x2="0" y2="1">
        <stop offset="0" stop-color="#dfe8ee"/><stop offset="1" stop-color="#9fadb7"/>
      </linearGradient>
      <linearGradient id="limePhoto" x1="0" y1="0" x2="1" y2="1">
        <stop offset="0" stop-color="#c7d8e6"/><stop offset="0.45" stop-color="#d8e3a4"/><stop offset="1" stop-color="#a9b76e"/>
      </linearGradient>
      <linearGradient id="officePhoto" x1="0" y1="0" x2="0" y2="1">
        <stop offset="0" stop-color="#e9edf0"/><stop offset="1" stop-color="#b8c0c6"/>
      </linearGradient>
      <linearGradient id="unitPhoto" x1="0" y1="0" x2="0" y2="1">
        <stop offset="0" stop-color="#7a7f83"/><stop offset="1" stop-color="#2e3134"/>
      </linearGradient>
      <linearGradient id="orangePhoto" x1="0" y1="0" x2="1" y2="0">
        <stop offset="0" stop-color="#e08a4c"/><stop offset="1" stop-color="#b9592a"/>
      </linearGradient>
    </defs>

    <rect x="0" y="0" width="330" height="360" fill="url(#skyPhoto)" role="img" aria-label="Photo of white shipping containers stacked outdoors"/>

    <polygon points="0,470 380,120 420,120 0,510" fill="var(--green)"/>
    <polygon points="0,540 460,120 480,120 0,560" fill="var(--lime)"/>
    <polygon points="330,0 380,0 330,46" fill="var(--green-dark)"/>

    <polygon points="405,22 900,22 900,440 590,440" fill="var(--green)"/>
    <polygon points="420,36 900,36 900,426 600,426" fill="url(#limePhoto)" role="img" aria-label="Photo of a new 40 foot pale green shipping container"/>

    <polygon points="640,440 900,440 900,1100 250,1100 250,1000" fill="var(--white)"/>
    <polygon points="900,470 900,1100 410,1100" fill="var(--white)"/>
    <polygon points="440,560 900,560 900,1100 440,1100" fill="var(--white)"/>
    <polygon points="440,560 640,440 900,440 900,560" fill="var(--white)"/>

    <polygon points="900,860 900,882 430,1014 430,992" fill="var(--navy)"/>

    <polygon points="400,395 560,555 400,715 240,555" fill="var(--green)"/>
    <polygon points="400,410 545,555 400,700 255,555" fill="var(--white)"/>

    <polygon points="140,600 300,600 300,770 170,770" fill="var(--slate)"/>
    <polygon points="215,590 315,690 215,790 115,690" fill="var(--white)"/>
    <polygon points="215,602 303,690 215,778 127,690" fill="url(#unitPhoto)" role="img" aria-label="Photo of a container interior fitted out as storage"/>

    <polygon points="215,800 315,900 215,1000 115,900" fill="var(--white)"/>
    <polygon points="215,812 303,900 215,988 127,900" fill="url(#orangePhoto)" role="img" aria-label="Photo of storage unit doors in orange"/>

    <rect x="500" y="920" width="380" height="170" fill="url(#officePhoto)" role="img" aria-label="Photo of a container converted into a mobile office with glass doors"/>

    <rect x="0" y="1100" width="900" height="100" fill="var(--charcoal)"/>
    <polygon points="0,1100 420,1100 380,1120 0,1120" fill="var(--green)"/>
  </svg>

  <div class="brand"><span class="brand-mark"></span>Corran<br>Management</div>

  <h1 class="headline">
    <span class="accent">We provide new and</span>
    <span class="dark">used containers</span>
    <span class="dark">to customers for</span>
  </h1>

  <ul class="uses uses-main">
    <li>Various reasons</li>
    <li>Mainly storage</li>
    <li>We also custom modify containers into storage units</li>
    <li>Mobile offices</li>
    <li>Mobile job site storage</li>
    <li>Command centers</li>
  </ul>
  <ul class="uses uses-more">
    <li>Pump houses</li>
    <li>Garages</li>
    <li>Living space</li>
    <li>The only limit is the Customers Imagination</li>
  </ul>

  <p class="call">Call today<span class="number">0100 555 0199</span></p>
</main>
</body>
</html>
```